BUSINESS CARD needed for TRAVEL BUSINESS

-Background-

Wandorvist Crew (WC) is a newly found company in Asia that trains and develops people with various demographics to become a FREQUENT TRAVELER & an ENTREPRENEUR combined. Basically, the core product that the company markets teaches people how to TRAVEL leisurely and yet EARN MONEY at the same time. Our main quote will be LIVING LIFE BY LIVING.

- The Job -

We will be constantly going out to different events, whether opening promotional booths in roadshows or at colleges or going for networking events. Thus we need a BUSINESS CARD design that portrays our POSITIONING & BRANDING

- Positioning -

TRAVEL LEISURELY & EARN at the SAME TIME

- Objective -

Serve as a BTL marketing & networking tool

- Target Audience -

Male & Females aged 19 - 35 who LOVES to TRAVEL & have strong aspirations to make it big and attaining financial freedom. The audience are enthusiastic and when they see an opportunity, they will seize it on the very spot. They are well connected and have a wide social network.

- Single Minded Proposition -

WC is My Dream Life

Target Market(s)

REFER TO CREATIVE BRIEF

Industry/Entity Type

Marketing

Requirements
Must have
• 1) The business card must portray a branding thats related to TRAVEL.

Boarding pass design was what we came up with but express your creativity and surprise me with better ideas. :)
Nice to have
• This is an idea that we have and we would most likely like to use however I do not want to restrict your creativity so i am putting in NICE TO HAVE instead.

Our idea design -> To have the namecard in the format of a BOARDING PASS lookalike

(You may refer to these weblink for inspiration -> https://www.pictofind.example/search?hl=en&q=boarding+pass&bav=on.2,or.r_gc.r_pw.r_cp.r_qf.,cf.osb&biw=1366&bih=667&um=1&ie=UTF-8&tbm=isch&source=og&sa=N&tab=wi&ei=l-f9T4KqC4fWrQfx8eC-Bg

or simply PICTOFIND BOARDING PASS IMAGES

```html
<!DOCTYPE html>
<html lang="en">
<head>
<meta charset="utf-8">
<title>Wandorvist Crew – Business Card</title>
<link rel="stylesheet" href="https://fonts.googleapis.com/css2?family=Kalam:wght@400&display=swap">
<style>
  :root {
    --backdrop: #2b3036;
    --card-white: #ffffff;
    --brand-red: #a41d20;
    --photo-red: #c23a34;
    --photo-grey: #9a9691;
    --photo-light: #d9d4cc;
    --ink: #2a2a2a;
    --rule: #b9b9b9;
    --postmark-tint: #fbe3d6;
  }
  * { margin: 0; padding: 0; box-sizing: border-box; }
  html, body { width: 1200px; height: 540px; overflow: hidden; }
  body {
    background: var(--backdrop);
    font-family: "Kalam", cursive;
    color: var(--ink);
    position: relative;
  }

  /* Front side */
  .card-front {
    position: absolute;
    left: 80px; top: 99px;
    width: 529px; height: 371px;
    border-radius: 25px;
    overflow: hidden;
  }
  .travel-photo {
    position: absolute; inset: 0;
    background: linear-gradient(100deg, var(--photo-light) 0%, var(--photo-grey) 45%, var(--photo-red) 100%);
  }
  .brand-panel {
    position: absolute;
    left: 290px; top: 87px;
    width: 206px; height: 189px;
    background: var(--brand-red);
  }
  .brand-mark {
    position: absolute;
    left: 300px; top: 18px;
    display: flex; align-items: center; gap: 8px;
  }
  .brand-mark__dot {
    width: 46px; height: 46px; border-radius: 50%;
    background: var(--card-white);
  }
  .brand-mark__name {
    font-size: 20px; color: var(--card-white);
  }

  /* Back side */
  .card-back {
    position: absolute;
    left: 635px; top: 99px;
    width: 499px; height: 318px;
    border-radius: 25px;
    background: var(--card-white);
  }
  .postmark {
    position: absolute;
    left: 294px; top: 22px;
    width: 128px; height: 54px;
    border-radius: 27px;
    background: var(--postmark-tint);
  }
  .stamp {
    position: absolute;
    left: 432px; top: 20px;
    width: 50px; height: 50px;
    padding: 4px;
    border: 1px dashed var(--rule);
  }
  .stamp__picture {
    width: 100%; height: 100%;
    background: var(--brand-red);
  }
  .tagline {
    position: absolute;
    left: 42px; top: 66px;
    font-size: 24px;
    transform: rotate(-6deg);
    transform-origin: left center;
  }
  .contact-note {
    position: absolute;
    left: 48px; top: 142px;
    width: 150px;
    font-size: 16px; line-height: 24px;
    text-align: center;
  }
  .contact-fields {
    position: absolute;
    left: 245px; top: 112px;
    width: 240px;
    list-style: none;
  }
  .contact-fields li {
    height: 46px;
    padding-top: 6px;
    font-size: 21px;
    text-align: center;
    border-bottom: 2px dashed var(--rule);
  }
  .contact-fields li:last-child { height: 34px; padding-top: 0; }
</style>
</head>
<body>

<section class="card-front">
  <div class="travel-photo" role="img" aria-label="Photo of cheerful travellers leaning out of a red and grey train window"></div>
  <div class="brand-panel"></div>
  <div class="brand-mark">
    <span class="brand-mark__dot"></span>
    <span class="brand-mark__name">WC</span>
  </div>
</section>

<section class="card-back">
  <div class="postmark" role="img" aria-label="Orange postal cancellation mark"></div>
  <div class="stamp">
    <div class="stamp__picture" role="img" aria-label="Postage stamp picture of a vintage plane"></div>
  </div>

  <p class="tagline">Living life by living...</p>

  <p class="contact-note">Thanks to contact me if you need more details about Wandorvist Crew</p>

  <ul class="contact-fields">
    <li>John Smith</li>
    <li>1234567890</li>
    <li>johnsmith@WC.com</li>
    <li>ASIA</li>
  </ul>
</section>

</body>
</html>
```